Smartphone App
Zielgruppe
Wir vertreiben ein Produkt (Name: Vorlix) mit dem Smartphone Apps erstellt werden können, quasi ein CMS für Smartphone Apps. Wir verkaufen dem Kunden das Produkt und dazu die Dienstleistung das Produkt beim Kunden zu installieren und zu personalisieren Analog zur Einrichtung eines CMS für eine Webseite.
Aufgabenstellung
Wir benötigen einen Flyer A4 den wir per Briefpost zur Kaltaquise versenden können.
Die Message die wir transportieren möchten ist, dass man heute mit einer Smartphone App neue Möglichkeiten hat, Informationen zum Kunden (Stammkunden) zu kommunizieren. Dass es einfach und schnell geht, eine eigene App zu haben und dass die Pflege kinderleicht ist und keine Fachkenntnisse erfordert. Schlagworte bezügl. der Funktionen der App: Informationen, Push-Nachrichten, Terminkalender, Reservierung, Verkauf, Bestellung. Der Leser soll neugierig darauf werden und einen Termin für eine unverbindliche Beratung vereinbaren. Bilder sollten Smartphone und Kundenbindung rüberbringen. Das Design sollte die Zielgruppe Gastronomen und Einzelhändler, also in der Regel Inhaber geführte Geschäfte ansprechen. Auf den Flyer sollten Informationen zu uns sein.

```html
<!DOCTYPE html>
<html lang="de">
<head>
<meta charset="utf-8">
<title>Vorlix Flyer</title>
<link href="https://fonts.googleapis.com/css2?family=Cabin:wght@400;500;600;700&family=Roboto+Condensed:wght@400;700&display=swap" rel="stylesheet">
<style>
  :root{
    --green:#6aae60;
    --green-dark:#4f8857;
    --white:#ffffff;
    --bg:#ffffff;
    --photo-light:#cfd3cf;
    --photo-mid:#b59c82;
    --photo-deep:#8a6e58;
    --hand-light:#e4ebf0;
    --hand-deep:#a9bccb;
    --device:#3a3d3b;
    --device-screen:#6b7a5a;
  }
  *{margin:0;padding:0;box-sizing:border-box}
  html,body{width:1200px;height:1200px;overflow:hidden;background:var(--bg)}
  .canvas{position:relative;width:1200px;height:1200px}
  .page{position:absolute;top:285px;width:436px;height:615px;background:var(--green);overflow:hidden;color:var(--white);font-family:"Cabin",sans-serif}
  .page--front{left:87px}
  .page--back{left:677px}

  /* Front */
  .front-art{position:absolute;left:0;top:0;width:436px;height:420px}
  .front-headline{position:absolute;left:31px;top:385px;font-size:46px;line-height:52px;font-weight:500}
  .front-claims{position:absolute;left:31px;top:448px;font-size:20px;line-height:31px;font-weight:500}
  .front-signature{position:absolute;right:8px;top:518px;font-size:17px;font-weight:700}
  .social-band{position:absolute;left:0;top:559px;width:436px;height:26px;background:var(--green-dark);display:flex;justify-content:center;align-items:center;gap:12px;font-family:"Roboto Condensed",sans-serif;font-size:11px;letter-spacing:.5px}
  .social-item{display:flex;align-items:center;gap:4px}
  .social-item::before{content:"";width:12px;height:12px;background:var(--white);opacity:.85}

  /* Back */
  .back-topbar{position:absolute;left:0;top:0}
  .back-headline{position:absolute;left:33px;top:30px;font-size:25px;line-height:27px;font-weight:500;color:var(--green)}
  .feature{position:absolute;font-family:"Roboto Condensed",sans-serif;font-weight:700;font-size:12.5px;line-height:17px}
  .feature--a{left:15px;top:156px}
  .feature--b{left:278px;top:244px}
  .feature--c{left:17px;top:304px}
  .feature--d{left:228px;top:352px}
  .screen-badge{position:absolute;border-radius:50%;border:5px solid var(--white);background:radial-gradient(circle at 45% 45%,var(--device-screen),var(--device) 70%)}
  .screen-badge--top{left:216px;top:108px;width:116px;height:116px}
  .screen-badge--low{left:152px;top:194px;width:116px;height:116px}
  .back-cta{position:absolute;left:26px;top:460px;font-size:21px;line-height:30px;font-weight:500}
  .back-footer{position:absolute;left:0;top:546px}
  .contact-row{position:absolute;left:0;top:578px;width:436px;height:37px;display:flex;justify-content:space-around;align-items:center;padding:0 8px;font-family:"Roboto Condensed",sans-serif;font-weight:700;font-size:12px;color:var(--green)}
</style>
</head>
<body>
<div class="canvas">

  <section class="page page--front">
    <svg class="front-art" viewBox="0 0 436 420" width="436" height="420">
      <defs>
        <linearGradient id="teamTone" x1="0" y1="0" x2="0" y2="1">
          <stop offset="0" stop-color="var(--photo-light)"/>
          <stop offset=".6" stop-color="var(--photo-mid)"/>
          <stop offset="1" stop-color="var(--photo-deep)"/>
        </linearGradient>
        <linearGradient id="handTone" x1="0" y1="0" x2="1" y2="1">
          <stop offset="0" stop-color="var(--hand-light)"/>
          <stop offset="1" stop-color="var(--hand-deep)"/>
        </linearGradient>
      </defs>
      <rect role="img" aria-label="Foto: junge Gruppe am Tisch mit Smartphones und Tablets" width="436" height="340" fill="url(#teamTone)"/>
      <path d="M0 200 C120 262 300 300 436 330 L436 420 L0 420 Z" fill="var(--green-dark)"/>
      <path d="M0 222 C140 292 300 320 436 350 L436 420 L0 420 Z" fill="var(--green)"/>
      <circle cx="96" cy="326" r="56" fill="var(--green-dark)"/>
      <circle role="img" aria-label="Foto: Handschlag" cx="96" cy="326" r="46" fill="url(#handTone)"/>
    </svg>
    <h1 class="front-headline">Ihre eigene App,</h1>
    <p class="front-claims">kinderleicht &amp; ohne Fachkentnisse.<br>sofort verfügbar &amp; einfachste Bedienung.</p>
    <p class="front-signature">mit Vorlix®</p>
    <div class="social-band">
      <span class="social-item">VORLIX</span>
      <span class="social-item">VORLIX</span>
      <span class="social-item">VORLIX</span>
    </div>
  </section>

  <section class="page page--back">
    <svg class="back-topbar" viewBox="0 0 436 160" width="436" height="160">
      <path d="M0 32 L436 32 L436 74 C320 95 190 132 0 150 Z" fill="var(--white)"/>
    </svg>
    <h2 class="back-headline">Optimieren Sie ihr Geschäft und<br>bieten ihren Kunden optimale<br>Möglichkeiten an.</h2>

    <div class="screen-badge screen-badge--top" role="img" aria-label="Bild: App auf Smartphone und Smartwatch"></div>
    <div class="screen-badge screen-badge--low" role="img" aria-label="Bild: App auf Tablet und Smartphone"></div>

    <p class="feature feature--a">Durch ihre eigene App,<br>können Sie mit ihren Kunden<br>besser kommunizieren und<br>ihr Geschäft vermarkten.</p>
    <p class="feature feature--b">Die App beinhaltet beis-<br>pielsweise Push-Nachrich-<br>ten mit der Sie ihre Infor-<br>mationen direkt an die<br>Kunden vermitteln können.</p>
    <p class="feature feature--c">Aber auch Reservierungen<br>oder Bestellungen sind mit<br>der App sofort realisierbar.</p>
    <p class="feature feature--d">Zudem gibt es noch weitere<br>Features der App, die je nach<br>Unternehmen verwendet<br>werden können.</p>

    <p class="back-cta">Falls ihre Interesse geweckt wurde, ve-<br>reinbaren Sie doch einfach einen Termin<br>für eine professionelle Beratung !</p>

    <svg class="back-footer" viewBox="0 0 436 69" width="436" height="69">
      <path d="M0 22 C140 0 300 0 436 22 L436 69 L0 69 Z" fill="var(--green-dark)"/>
      <rect x="0" y="32" width="436" height="37" fill="var(--white)"/>
    </svg>
    <div class="contact-row">
      <span>ITSERVICE-PARTNER</span>
      <span>JONAS MERBECK</span>
      <span>LINDENAU</span>
      <span>TEL.: 02345-610482</span>
    </div>
  </section>

</div>
</body>
</html>
```